Speisekarten-Design für HotDog-/Eis-Laden
Zielgruppe
'Fensterverkauf von HotDogs und Frozen Joghurt.'
Wir eröffnen einen kleinen HotDog/Eis Laden in einer U-Bahn Station in direkter Nähe zum Stadtpark. Unsere Zielgruppe sind Schüler, Touristen, Spazierengänger und U-Bahn Fahrer.
Aufgabenstellung
Bei der Haltestelle handelt es sich um ein denkmalgeschützes Gebäude. Deswegen stellen wir uns eine Speisekarte im Retrostil vor, welches wir an die Scheibe anbringen wollen. Als Vorstellung habe ich die Speisekarten im alten Fastfood Stil der 50er Jahre (Brumfields etc.). Die Maße der Scheibe beträgt 120x54cm(HxB). Das von mir beispielhaft zusammengestellte Menü dient als richtungsweisend. Trotzdem bin ich offen für gegen Vorschläge.
Die Produkte entsprechen ungefähr dem was wir anbieten werden, wurden jedoch nicht weiter ausgeschrieben oder Kalkuliert. Den tatsächlichen Inhalt würde ich zeitnah nachreichen.

```html
<!DOCTYPE html>
<html lang="de">
<head>
<meta charset="utf-8">
<title>The Kind Pals – Speisekarte</title>
<link href="https://fonts.googleapis.com/css2?family=Archivo+Black&family=Josefin+Sans:wght@300;400&display=swap" rel="stylesheet">
<style>
  :root {
    --menu-red: #c14a3d;
    --menu-red-dark: #a93a31;
    --cream: #e9cf96;
    --cream-soft: #f0dcaa;
  }
  * { margin: 0; padding: 0; box-sizing: border-box; }
  html, body { width: 1200px; height: 2400px; overflow: hidden; background: var(--cream); }
  .menu-board {
    position: relative; width: 1200px; height: 2400px;
    background: var(--cream);
    font-family: "Archivo Black", "Arial Black", sans-serif;
    color: var(--cream);
  }
  .menu-panel {
    position: absolute; left: 47px; right: 47px; top: 0; bottom: 0;
    background:
      radial-gradient(ellipse at 30% 20%, rgba(255,255,255,0.05), transparent 60%),
      radial-gradient(ellipse at 70% 80%, rgba(0,0,0,0.06), transparent 60%),
      var(--menu-red);
  }
  .abs { position: absolute; }
  .center { left: 0; right: 0; text-align: center; }
  .brand-name {
    top: 60px; font-size: 96px; line-height: 1.0; letter-spacing: 1px;
  }
  .banner {
    background: var(--cream); color: var(--menu-red-dark);
    text-align: center; transform: rotate(-1.2deg);
  }
  .banner-city { left: 108px; width: 772px; top: 327px; height: 96px; font-size: 58px; line-height: 96px; letter-spacing: 1px; }
  .district { top: 430px; font-family: "Josefin Sans", sans-serif; font-weight: 300; font-size: 48px; letter-spacing: 4px; }
  .icon-box { background: var(--cream); border-radius: 40px; opacity: 0.95; }
  .icon-hotdog { left: 127px; top: 502px; width: 128px; height: 86px; }
  .icon-froyo { left: 880px; top: 490px; width: 82px; height: 104px; border-radius: 40px 40px 10px 10px; }
  .section-head { font-size: 40px; line-height: 1.2; text-align: center; }
  .head-hotdogs { left: 270px; top: 500px; width: 230px; }
  .head-hotdogs small { display: block; font-family: "Josefin Sans", sans-serif; font-size: 20px; line-height: 1; }
  .head-froyo { left: 590px; top: 500px; width: 270px; }
  .item { width: 446px; }
  .item-row { display: flex; justify-content: space-between; font-size: 29px; line-height: 1.1; }
  .item-desc { font-family: "Josefin Sans", sans-serif; font-size: 18px; letter-spacing: 2px; line-height: 1.5; text-transform: uppercase; margin-top: 4px; }
  .item-desc b { font-family: "Archivo Black", sans-serif; font-weight: 400; font-size: 28px; letter-spacing: 0; }
  .col-left { left: 75px; }
  .col-right { left: 593px; }
  .deal-intro { top: 1180px; font-size: 60px; letter-spacing: 1px; }
  .deal-word { top: 1228px; font-size: 150px; line-height: 1; letter-spacing: 4px; }
  .banner-student { left: 188px; width: 565px; top: 1420px; height: 58px; font-size: 44px; line-height: 58px; transform: none; }
  .light-line { font-family: "Josefin Sans", sans-serif; font-weight: 400; font-size: 38px; letter-spacing: 6px; }
  .bold-line { font-size: 44px; }
  .list-head { font-size: 40px; }
  .list { width: 445px; }
  .list-right { left: 635px; width: 393px; }
  .list .item-row { font-size: 29px; line-height: 40px; }
  .open-line { top: 2190px; font-size: 70px; }
  .open-line span { font-size: 48px; }
  .hours { top: 2270px; font-size: 50px; }
  .address { top: 2338px; font-family: "Josefin Sans", sans-serif; font-size: 26px; letter-spacing: 4px; }
</style>
</head>
<body>
<main class="menu-board">
  <section class="menu-panel">
    <h1 class="abs center brand-name">THE KIND<br>PALS</h1>
    <div class="abs banner banner-city">RETRO CITY BAR</div>
    <p class="abs center district">WINTERHUDE</p>

    <div class="abs icon-box icon-hotdog" role="img" aria-label="Hot-Dog-Symbol"></div>
    <h2 class="abs section-head head-hotdogs">HOT<br>DOGS<small>100%BEEF</small></h2>
    <h2 class="abs section-head head-froyo">FROZEN<br>JOGHURT</h2>
    <div class="abs icon-box icon-froyo" role="img" aria-label="Frozen-Joghurt-Becher-Symbol"></div>

    <div class="abs item col-left" style="top:655px">
      <div class="item-row"><span>CLASSIC</span><span>3.00€</span></div>
      <p class="item-desc">Rinderwurst, Gurken, Ketchup<br>Senf, Röstzwiebel</p>
    </div>
    <div class="abs item col-left" style="top:785px">
      <div class="item-row"><span>CHEESE</span><span>4.00€</span></div>
      <p class="item-desc">Rinderwurst, Gurken, Ketchup<br>Senf, Röstzwiebe, Nachos,Hot<br>Cheese</p>
    </div>
    <div class="abs item col-left" style="top:914px">
      <div class="item-row"><span>JALAPENOS</span><span>4.20€</span></div>
      <p class="item-desc">Rinderwurst, Jalapenos,Salsa-<br>sauce, Röstzwiebel, Nachos,<br>Hot Cheese</p>
    </div>
    <div class="abs item col-left" style="top:1035px">
      <div class="item-row"><span>DOUBLE PACK</span><span>5.00€</span></div>
      <p class="item-desc">2 Rinderwurst, Gurken, Ketchup<br>Senf, Röstzwiebel</p>
    </div>

    <div class="abs item col-right" style="top:655px">
      <div class="item-row"><span>SMALL</span><span>3.50€</span></div>
      <p class="item-desc">Frozen Joghurt+1 Topping&amp;Sauce</p>
    </div>
    <div class="abs item col-right" style="top:785px">
      <div class="item-row"><span>MEDIUM</span><span>4.00€</span></div>
      <p class="item-desc">Frozen Joghurt+2 Topping</p>
    </div>
    <div class="abs item col-right" style="top:914px">
      <div class="item-row"><span>LARGE</span><span>4.00€</span></div>
      <p class="item-desc">Gurkeneis, Jalapenos</p>
    </div>
    <div class="abs item col-right" style="top:1035px">
      <p class="item-desc"><b>TOPPING:</b> Schoko, Erdbeere,<br>Karamell<br><b>SAUCEN:</b> Schoko, Erdbeere,<br>Karamell</p>
    </div>

    <p class="abs center deal-intro">THE GOOD</p>
    <p class="abs center deal-word">DEAL</p>
    <div class="abs banner banner-student">STUDENT SPECIAL</div>
    <p class="abs center light-line" style="top:1490px">ALL STUDENT GETS 10% OFFER!</p>
    <p class="abs center bold-line" style="top:1540px">STADTPARK SPECIAL</p>
    <p class="abs center light-line" style="top:1600px">5 SAME PRODUCTS ONE FOR FREE!</p>

    <div class="abs list col-left" style="top:1670px">
      <h3 class="list-head">SHAVED ICE</h3>
      <div style="margin-top:28px">
        <div class="item-row"><span>SMALL</span><span>3.00€</span></div>
        <div class="item-row"><span>MEDIUM</span><span>4.00€</span></div>
        <div class="item-row"><span>LARGE</span><span>4.00€</span></div>
        <p class="item-desc" style="margin-top:0">Blaubeere, Waldmeister, Kirsche</p>
      </div>
    </div>
    <div class="abs list list-right" style="top:1670px">
      <h3 class="list-head">MILK SHAKE</h3>
      <div style="margin-top:28px">
        <div class="item-row"><span>SMALL</span><span>3.00€</span></div>
        <div class="item-row"><span>MEDIUM</span><span>4.00€</span></div>
        <div class="item-row"><span>LARGE</span><span>4.00€</span></div>
        <p class="item-desc" style="margin-top:0">Schoko, Erdbeere, Karamell</p>
      </div>
    </div>

    <div class="abs list col-left" style="top:1918px">
      <h3 class="list-head">EXTRAS</h3>
      <div style="margin-top:28px">
        <div class="item-row"><span>VEGANE WURST</span><span>0.70€</span></div>
        <div class="item-row"><span>GLUTENFREI BUN</span><span>1.00€</span></div>
        <div class="item-row"><span>HOT CHEESE</span><span>4.00€</span></div>
        <div class="item-row"><span>JALAPENOS</span><span>1.00€</span></div>
      </div>
    </div>
    <div class="abs list list-right" style="top:1918px">
      <h3 class="list-head">SOFTDRINKS</h3>
      <div style="margin-top:28px">
        <div class="item-row"><span>COLA</span><span>3.00€</span></div>
        <div class="item-row"><span>COLA LIGHT</span><span>3.00€</span></div>
        <div class="item-row"><span>WASSER</span><span>2.50€</span></div>
      </div>
    </div>

    <p class="abs center open-line">OPEN <span>7 DAYS A WEEK</span></p>
    <p class="abs center hours">11 AM TO 9 PM</p>
    <p class="abs center address">THE KIND PALS, LINDENWEG 12, 22301 HAMBURG</p>
  </section>
</main>
</body>
</html>
```